Academic and Business book cover

I need a book cover for my academic and business book.
The focus is in international / global negotiation and influence (how to negotiate across cultures).
The book will be published on Brevora, both in Lumaro and printed edition. therefore I need something that works under Brevora guidelines.The final design should be elegant and still be able to stand out against the competition.
I would like to have orange+grey for the text colors on the cover, even if different options are welcome.
Title and my name are in the attached word doc.

Target Market(s)

graduates, Phds, from international business schools. Managers

Industry/Entity Type

Business

Font styles to use
Serif
Sans Serif

Colors

Requirements
Must have
• The title and my name should have elegant fonts.
Nice to have
• pictures of the world that don't have the "usual" Europe in the centre.

```html
<!DOCTYPE html>
<html lang="en">
<head>
<meta charset="utf-8">
<title>The 4Cs Playbook — Book Cover</title>
<link rel="stylesheet" href="https://fonts.googleapis.com/css2?family=Marcellus&family=Marcellus+SC&display=swap">
<style>
  :root {
    --stage: #5e5e5e;
    --paper: #ffffff;
    --orange: #fb7e48;
    --grey-text: #7a7c7e;
    --dot-blue: #b8c9d3;
    --dot-stone: #dedfd6;
    --dot-slate: #75787a;
    --dot-orange: #fd7f47;
  }
  html, body {
    margin: 0;
    padding: 0;
    width: 1200px;
    height: 1000px;
    overflow: hidden;
    background: var(--stage);
  }
  .canvas {
    position: relative;
    width: 1200px;
    height: 1000px;
    background: var(--stage);
  }
  .cover {
    position: absolute;
    left: 340px;
    top: 87px;
    width: 517px;
    height: 828px;
    background: var(--paper);
  }
  .title {
    position: absolute;
    left: 0;
    top: 66px;
    width: 100%;
    margin: 0;
    text-align: center;
    font-family: "Marcellus", serif;
    font-weight: 400;
    font-size: 86px;
    line-height: 74px;
    letter-spacing: -1.5px;
    color: var(--orange);
  }
  .subtitle {
    position: absolute;
    left: 0;
    top: 230px;
    width: 100%;
    margin: 0;
    text-align: center;
    font-family: "Marcellus", serif;
    font-size: 19px;
    line-height: 24px;
    color: var(--grey-text);
  }
  .pillars {
    position: absolute;
    left: 98px;
    top: 344px;
    width: 320px;
    height: 320px;
  }
  .pillars text {
    font-family: "Marcellus", serif;
    font-size: 56px;
    fill: #ffffff;
  }
  .author {
    position: absolute;
    left: 0;
    top: 745px;
    width: 100%;
    margin: 0;
    text-align: center;
    font-family: "Marcellus SC", serif;
    font-size: 33px;
    letter-spacing: 0.3px;
    color: var(--grey-text);
  }
</style>
</head>
<body>
  <main class="canvas">
    <section class="cover">
      <h1 class="title">The 4Cs<br>Playbook</h1>
      <p class="subtitle">Practical Bargaining and Persuasion Methods<br>for Cross-Cultural Success</p>
      <svg class="pillars" viewBox="0 0 320 320" aria-label="Four C pillars">
        <circle cx="78" cy="79" r="78" fill="var(--dot-slate)"/>
        <circle cx="240" cy="79" r="78" fill="var(--dot-blue)"/>
        <circle cx="78" cy="241" r="78" fill="var(--dot-orange)"/>
        <circle cx="240" cy="241" r="78" fill="var(--dot-stone)"/>
        <text x="78" y="99" text-anchor="middle">C</text>
        <text x="240" y="99" text-anchor="middle">C</text>
        <text x="78" y="261" text-anchor="middle">C</text>
        <text x="240" y="261" text-anchor="middle">C</text>
      </svg>
      <p class="author">Harvinder K. Solan</p>
    </section>
  </main>
</body>
</html>
```